Merrow Consulting needs a business card design

Merrow Consulting is a small business that consults and trains Australia wide in Workplace Health and Safety, Environment and Quality Management Systems.

Clients are typically smaller businesses with 50 to 200 employees but there are some large clients.

Communication is often by email, although mobile is used as well.

Merrow Consulting
41 Tulwin Ferris Road
Brindale, QLD 4215
0438 291 064

```html
<!DOCTYPE html>
<html lang="en">
<head>
<meta charset="utf-8">
<title>Merrow Consulting – Business Card Concepts</title>
<link href="https://fonts.googleapis.com/css2?family=Open+Sans:wght@400;700&family=Didact+Gothic&display=swap" rel="stylesheet">
<style>
  :root {
    --backdrop: #e0e0de;
    --card: #ffffff;
    --green: #41b384;
    --charcoal: #4b4742;
    --white: #ffffff;
  }
  * { margin: 0; padding: 0; box-sizing: border-box; }
  html, body {
    width: 1200px;
    height: 900px;
    overflow: hidden;
    background: var(--backdrop);
  }
  .sheet {
    position: relative;
    width: 1200px;
    height: 900px;
  }
  .card {
    position: absolute;
    width: 419px;
    height: 239px;
    background: var(--card);
    overflow: hidden;
  }
  .card--one   { left: 166px; top: 60px; }
  .card--two   { left: 615px; top: 60px; }
  .card--three { left: 166px; top: 330px; }
  .card--four  { left: 615px; top: 330px; }
  .card--five  { left: 406px; top: 600px; }

  .block {
    position: absolute;
    top: 80px;
    height: 79px;
  }
  .block--name { left: 0; width: 210px; }
  .block--contact { left: 210px; width: 209px; }
  .block--green { background: var(--green); }
  .block--charcoal { background: var(--charcoal); }
  .block--rounded { left: 206px; width: 213px; border-top-left-radius: 28px; }
  .block--plain { left: 206px; width: 213px; }
  .accent-strip {
    position: absolute;
    top: 80px;
    left: 406px;
    width: 13px;
    height: 79px;
  }

  .brand {
    position: absolute;
    left: 25px;
    top: 80px;
    height: 79px;
    display: flex;
    align-items: center;
    font-family: "Open Sans", sans-serif;
    font-size: 19px;
    font-weight: 400;
    letter-spacing: -0.2px;
    white-space: nowrap;
  }
  .brand strong { font-weight: 700; }
  .brand--light { color: var(--white); }
  .brand--dark { color: var(--charcoal); }
  .brand--green { color: var(--green); }

  .contact {
    position: absolute;
    top: 80px;
    height: 79px;
    display: flex;
    flex-direction: column;
    justify-content: center;
    font-family: "Didact Gothic", sans-serif;
    font-style: normal;
    font-size: 16.5px;
    line-height: 17.6px;
    white-space: nowrap;
    padding-top: 1px;
  }
  .contact--light { color: var(--white); }
  .contact--dark { color: var(--charcoal); }
  .contact--at-235 { left: 235px; }
  .contact--at-229 { left: 229px; }
  .contact--at-233 { left: 235px; }
</style>
</head>
<body>
<main class="sheet">

  <section class="card card--one">
    <div class="block block--name block--green"></div>
    <div class="block block--contact block--charcoal"></div>
    <p class="brand brand--light">Merrow&nbsp;<strong>Consulting</strong></p>
    <address class="contact contact--light contact--at-235">
      <span>41 Tulwin Ferris Road</span>
      <span>Brindale, QLD 4215</span>
      <span>0438 291 064</span>
    </address>
  </section>

  <section class="card card--two">
    <div class="block block--name block--charcoal"></div>
    <div class="accent-strip block--green"></div>
    <p class="brand brand--light">Merrow&nbsp;<strong>Consulting</strong></p>
    <address class="contact contact--dark contact--at-229">
      <span>41 Tulwin Ferris Road</span>
      <span>Brindale, QLD 4215</span>
      <span>0438 291 064</span>
    </address>
  </section>

  <section class="card card--three">
    <div class="block block--name block--green"></div>
    <div class="accent-strip block--charcoal"></div>
    <p class="brand brand--light">Merrow&nbsp;<strong>Consulting</strong></p>
    <address class="contact contact--dark contact--at-229">
      <span>41 Tulwin Ferris Road</span>
      <span>Brindale, QLD 4215</span>
      <span>0438 291 064</span>
    </address>
  </section>

  <section class="card card--four">
    <div class="block block--rounded block--green"></div>
    <p class="brand brand--dark">Merrow&nbsp;<strong>Consulting</strong></p>
    <address class="contact contact--light contact--at-233">
      <span>41 Tulwin Ferris Road</span>
      <span>Brindale, QLD 4215</span>
      <span>0438 291 064</span>
    </address>
  </section>

  <section class="card card--five">
    <div class="block block--plain block--green"></div>
    <p class="brand brand--green">Merrow&nbsp;<strong>Consulting</strong></p>
    <address class="contact contact--light contact--at-233">
      <span>41 Tulwin Ferris Road</span>
      <span>Brindale, QLD 4215</span>
      <span>0438 291 064</span>
    </address>
  </section>

</main>
</body>
</html>
```